Business Card for New Greek Restaurant

Looking for a Business card for a new Greek Restaurant that's focus is on Take out and Delivery & catering.

Also to outline the contact information for the restaurant.
Does not require a name or title of a specific person (Just general business card)
Phone (519) 731-FOOD (3663)
Email : info@bluefigkitchen.ca
Website : www.bluefigkitchen.ca

Facebook/Instagram/Twitter Icons to Follow us as well.

TAKEOUT * DELIVERY* CATERING

Target Market(s)

Woman Age 25-44

Industry/Entity Type

Greek Restaurant

Contact Information for Business Card

Card is to have the general contact information for the business as well as outline our Take Out and Catering Services. Existing Logo attached and to be incorporated into the design.

Font styles to use
Sans Serif

Colors

Designer to choose colors to be used in the design.

Requirements
Must have
• Restaurant Contact Information :
• Phone (519) 731-FOOD (3663)
• Email : info@bluefigkitchen.ca
• Website : www.bluefigkitchen.ca
• Highlight Takeout, Catering, Delivery
• Business Address :
• Maplerow Plaza
• 47 Carden Ave., Unit 6
• Breslau ON
• N0K 2P5
Nice to have
• Modern Feel to promote TakeOut and Catering Services.
Should not have
• No Specific Title or Contact Person (Generic Business Card for Restaurant)

```html
<!DOCTYPE html>
<html lang="en">
<head>
<meta charset="utf-8">
<title>Blue Fig Kitchen – Business Card</title>
<link href="https://fonts.googleapis.com/css2?family=PT+Sans:wght@400;700&display=swap" rel="stylesheet">
<style>
  :root {
    --backdrop: #e4e2df;
    --card-black: #0b0b0c;
    --card-glow: #2a2a2c;
    --brand-blue: #1aafe0;
    --band-grey: #b9babc;
    --band-dark: #6e6f72;
    --ink-white: #f4f4f4;
  }
  * { margin: 0; padding: 0; box-sizing: border-box; }
  html, body {
    width: 1200px; height: 962px; overflow: hidden;
    background: var(--backdrop);
    font-family: "PT Sans", sans-serif;
  }
  .canvas { position: relative; width: 1200px; height: 962px; }
  .card {
    position: absolute; left: 290px; width: 620px; height: 354px;
    border-radius: 14px; overflow: hidden;
    background: radial-gradient(ellipse at 50% 45%, var(--card-glow) 0%, var(--card-black) 65%);
    box-shadow: 0 10px 28px rgba(0,0,0,.25);
  }
  .card--front { top: 58px; }
  .card--back { top: 514px; }

  .social-row { position: absolute; top: 26px; right: 26px; display: flex; gap: 14px; }
  .social-row span { width: 30px; height: 30px; border-radius: 5px; background: var(--ink-white); }

  .brand-name {
    color: var(--brand-blue); font-weight: 700; text-transform: uppercase;
    letter-spacing: 3px; line-height: 1.05;
  }
  .card--front .brand-name {
    position: absolute; top: 110px; left: 0; width: 100%; text-align: center; font-size: 52px;
  }
  .services {
    position: absolute; top: 262px; width: 100%; text-align: center;
    color: var(--ink-white); font-size: 22px; letter-spacing: .5px;
  }
  .services strong { font-weight: 700; }

  .swoosh { position: absolute; inset: 0; }
  .card--back .brand-name {
    position: absolute; top: 150px; left: 36px; font-size: 36px; width: 220px;
  }
  .contact-list {
    position: absolute; top: 156px; left: 262px; list-style: none;
    color: var(--ink-white); font-size: 17px;
  }
  .contact-list li {
    display: flex; align-items: flex-start; gap: 12px; margin-bottom: 11px;
    line-height: 1.25; white-space: nowrap;
  }
  .contact-list svg { flex: none; width: 18px; height: 18px; margin-top: 1px; fill: var(--brand-blue); }
</style>
</head>
<body>
<main class="canvas">

  <section class="card card--front">
    <div class="social-row" aria-label="Social profiles">
      <span></span><span></span><span></span>
    </div>
    <h1 class="brand-name">Blue Fig<br>Kitchen</h1>
    <p class="services">TAKEOUT * <strong>DELIVERY</strong>* CATERING</p>
  </section>

  <section class="card card--back">
    <svg class="swoosh" viewBox="0 0 620 354" preserveAspectRatio="none">
      <rect width="620" height="354" fill="var(--brand-blue)"/>
      <path d="M0,36 C300,-10 620,20 620,250 V354 H0 Z" fill="var(--band-grey)"/>
      <path d="M0,62 C300,12 612,32 614,354 H0 Z" fill="var(--band-dark)"/>
      <path d="M0,70 C300,20 610,40 606,354 H0 Z" fill="var(--card-black)"/>
    </svg>
    <h2 class="brand-name">Blue Fig<br>Kitchen</h2>
    <ul class="contact-list">
      <li>
        <svg viewBox="0 0 20 20"><path d="M10 2 1 10h3v8h5v-5h2v5h5v-8h3z"/></svg>
        <span>Maplerow Plaza 47 Carden<br>Ave., Unit 6 Breslau ON N0K 2P5</span>
      </li>
      <li>
        <svg viewBox="0 0 20 20"><path d="M6 1h8a2 2 0 0 1 2 2v14a2 2 0 0 1-2 2H6a2 2 0 0 1-2-2V3a2 2 0 0 1 2-2zm0 3v11h8V4z"/></svg>
        <span>(519) 731-FOOD (3663)</span>
      </li>
      <li>
        <svg viewBox="0 0 20 20"><path d="M1 4h18v12H1zm2 2v.5l7 5 7-5V6l-7 5z"/></svg>
        <span>info@bluefigkitchen.ca</span>
      </li>
      <li>
        <svg viewBox="0 0 20 20"><circle cx="10" cy="10" r="8"/></svg>
        <span>www.bluefigkitchen.ca</span>
      </li>
    </ul>
  </section>

</main>
</body>
</html>
```